Grounded Tide Healing needs business card design

I need a business card design for a new energy healing business in Perth Australia. As an energy healer I am quite earthy and practical rather than floaty and fairydust.
One of the techniques I use is unique in Australia but used internationally (US, UK and Europe). I practice with Coastal Pathway Therapy, Reiki and massage as well as some other techniques I developed personally. I am starting to incorporate sound healing into my practice. I literally change people's lives. The potential for each client is wide open. A key skill I bring to my practice is the capacity for making difficult situations seem more fun and less stressful.
Clients are likely to be depressed, physically unwell, going through a difficult time, unhappy with their current situation. They are people looking for new options to solve a difficult existing problem. They have probably tried other avenues before they come to me. They are open to something different.

I would like to communicate that the client and I work together for their healing and personal growth. I would like to convey that while the work of changing is challenging it can also be fun.

Hi all, info required on the card is:

Name
Title: Healer
contact number (mobile)
I don''t have a logo - I would be interested in seeing designs that use the whole card as well as the traditional logo on one side / in one corner. Whatever ''look/feel'' I choose will carry over to the website as well.

thanks
Meg

Reason: One or two of the designs caught my eye and many appeal for different reasons, but nothing is quite right for me. I've invited a couple of other designers to contribute so I wanted to give them time to be involved. kind regards Meg

Thank you all for the fabulous designs. I really appreciated the thought that many people put into my brief and a number of designs captured important things about what I was trying to say. It was a hard choice between 3 designs in the end.
thanks again and kind regards
Meg

Target Market(s)

people looking for new options to solve a difficult existing problem

Industry/Entity Type

Massage

Logo styles of interest
Abstract Logo
Requirements
Must have
• include green and blue
Nice to have
• hands, tea / teapots , the ocean, stepping stones

```html
<!DOCTYPE html>
<html lang="en">
<head>
<meta charset="utf-8">
<title>Grounded Tide Healing – Business Card</title>
<link rel="stylesheet" href="https://fonts.googleapis.com/css2?family=Arimo:wght@400;700&family=Cormorant+Garamond:ital,wght@1,400;1,500&display=swap">
<style>
  :root {
    --card-white: #ffffff;
    --band-light: #c4e8f8;
    --band-mid: #9fd6f1;
    --band-edge: #7fc4e6;
    --sky-blue: #59bde8;
    --leaf-green: #2f8f3c;
    --ink: #111111;
  }
  html, body {
    margin: 0;
    padding: 0;
    overflow: hidden;
    background: var(--card-white);
  }
  .card {
    position: relative;
    width: 1200px;
    height: 777px;
    background: var(--card-white);
    overflow: hidden;
    font-family: "Arimo", Arial, sans-serif;
    color: var(--ink);
  }
  .side-band {
    position: absolute;
    left: 0;
    top: 0;
    width: 153px;
    height: 777px;
    background: linear-gradient(90deg, var(--band-light) 0%, var(--band-mid) 100%);
    border-right: 2px solid var(--band-edge);
  }
  .side-band__text {
    position: absolute;
    left: 77px;
    top: 388px;
    width: 600px;
    transform: translate(-50%, -50%) rotate(-90deg);
    text-align: center;
    font-family: "Cormorant Garamond", "Times New Roman", serif;
    font-style: italic;
    font-weight: 500;
    font-size: 34px;
    line-height: 54px;
    color: var(--ink);
  }
  .headline {
    position: absolute;
    left: 245px;
    top: 100px;
    margin: 0;
    font-family: "Cormorant Garamond", "Times New Roman", serif;
    font-style: italic;
    font-weight: 400;
    font-size: 136px;
    line-height: 1;
    color: var(--sky-blue);
  }
  .brand {
    position: absolute;
    left: 770px;
    top: 18px;
    width: 420px;
    text-align: center;
  }
  .brand__mark {
    display: block;
    margin: 0 auto;
  }
  .brand__name {
    margin-top: 30px;
    white-space: nowrap;
    font-family: "Arimo", Arial, sans-serif;
    font-weight: 700;
    font-size: 24px;
    letter-spacing: 0.5px;
    text-transform: uppercase;
    color: var(--leaf-green);
  }
  .divider {
    position: absolute;
    left: 230px;
    top: 268px;
    width: 941px;
    height: 3px;
    background: var(--leaf-green);
  }
  .concerns {
    position: absolute;
    font-size: 29px;
    line-height: 43px;
    margin: 0;
    padding: 0;
    list-style: none;
  }
  .concerns--left { left: 311px; top: 338px; }
  .concerns--left li:nth-child(2) { padding-left: 7px; }
  .concerns--right { left: 705px; top: 338px; }
  .question {
    position: absolute;
    left: 155px;
    width: 1045px;
    top: 526px;
    text-align: center;
    font-size: 41px;
    margin: 0;
  }
  .promise {
    position: absolute;
    left: 155px;
    width: 1045px;
    top: 628px;
    text-align: center;
    font-size: 29px;
    margin: 0;
  }
  .contact {
    position: absolute;
    left: 155px;
    width: 1045px;
    top: 708px;
    text-align: center;
    font-size: 25px;
    margin: 0;
    color: var(--leaf-green);
  }
  .contact__name { font-weight: 700; }
</style>
</head>
<body>
  <div class="card">
    <aside class="side-band">
      <div class="side-band__text">Coastal Pathway Therapy<br>Reiki and Massage</div>
    </aside>

    <h1 class="headline">Are you?</h1>

    <div class="brand">
      <svg class="brand__mark" width="150" height="150" viewBox="0 0 150 150" aria-hidden="true">
        <circle cx="75" cy="75" r="72" fill="var(--leaf-green)"/>
      </svg>
      <div class="brand__name">Grounded Tide Healing</div>
    </div>

    <div class="divider"></div>

    <ul class="concerns concerns--left">
      <li>Stressed</li>
      <li>Depressed</li>
      <li>Physically Unwell</li>
    </ul>
    <ul class="concerns concerns--right">
      <li>Tired</li>
      <li>Going through a difficult time</li>
    </ul>

    <p class="question">Are you running out of options?</p>
    <p class="promise">Have fun working with me as you heal and gain personal growth</p>
    <p class="contact"><span class="contact__name">Meg</span> &nbsp;·&nbsp; Healer &nbsp;·&nbsp; Mobile 0412 555 019</p>
  </div>
</body>
</html>
```